Roofing company in Toronto, Canada needs a logo design and business card design

We need a business card and logo created for our company. Our company is "KVL Roofing" which provides roofing services for commercial and residential customers. We serve customers in the Greater Toronto Area (in Canada) thus the name KVL.

We want the logo and business card to be a modern design displaying professionalism and quality in the work. We would prefer rounded corners for the business cards but are open to other ideas. The cards should be pleasant and appealing to customers.

Target Market(s)

Commercial and Residential customers

Industry/Entity Type

Roofing

Contact Information for Business Card

Logo Text

KVL Roofing

Requirements
Nice to have
• Colours that are pleasing to the eye but at the same time should stand out from other business cards. If the design can incorporate the name of KVL Roofing and the actual concept of roofing that would be nice.
Should not have
• Do not want the business cards or logo to be childish looking. Need to look professionally designed.

```html
<!DOCTYPE html>
<html lang="en">
<head>
<meta charset="utf-8">
<title>KVL Roofing – Business Card</title>
<link rel="stylesheet" href="https://fonts.googleapis.com/css2?family=PT+Sans:wght@400;700&display=swap">
<style>
  :root {
    --backdrop: #3b3531;
    --card: #141414;
    --gold: #e9a91b;
    --white: #f2f2f2;
    --grey: #cfcfcf;
  }
  * { box-sizing: border-box; margin: 0; padding: 0; }
  html, body {
    width: 1200px; height: 900px; overflow: hidden;
    background: var(--backdrop);
    font-family: "PT Sans", Arial, sans-serif;
  }
  .stage {
    width: 1200px; height: 900px;
    display: flex; align-items: center; justify-content: center; gap: 40px;
  }
  .card {
    width: 540px; height: 310px;
    background: var(--card);
    border-radius: 14px;
    position: relative;
    box-shadow: 0 10px 30px rgba(0,0,0,.45);
  }
  /* front */
  .card-front .brand-mark {
    position: absolute; left: 44px; bottom: 56px;
    display: flex; align-items: center; gap: 12px;
    color: var(--gold); font-weight: 700; font-size: 30px; letter-spacing: 1px;
  }
  .brand-mark .square { width: 16px; height: 16px; background: var(--gold); }
  .contact {
    position: absolute; left: 300px; top: 70px;
    color: var(--white); font-size: 14px; line-height: 1.35;
  }
  .contact .name { color: var(--gold); font-size: 21px; line-height: 1.1; }
  .contact .role { margin-bottom: 18px; }
  .contact .address { margin-bottom: 16px; }
  .contact ul { list-style: none; }
  .contact li { display: flex; align-items: center; gap: 10px; }
  .contact svg { width: 12px; height: 12px; fill: var(--gold); flex: none; }
  /* back */
  .card-back { display: flex; align-items: center; justify-content: center; }
  .brand-name {
    color: var(--gold); font-weight: 700; font-size: 56px;
    letter-spacing: 3px; text-transform: uppercase;
  }
</style>
</head>
<body>
<main class="stage">
  <section class="card card-front">
    <div class="brand-mark"><span class="square"></span><span>KVL Roofing</span></div>
    <div class="contact">
      <p class="name">Daniel Harper</p>
      <p class="role">Managing Director</p>
      <p class="address">48 Harbour Street East<br>Toronto, ON M5J 2L1.</p>
      <ul>
        <li><svg viewBox="0 0 24 24"><path d="M6.6 10.8a15.1 15.1 0 0 0 6.6 6.6l2.2-2.2c.3-.3.7-.4 1-.2 1.1.4 2.3.6 3.6.6.6 0 1 .4 1 1V20c0 .6-.4 1-1 1A17 17 0 0 1 3 4c0-.6.4-1 1-1h3.5c.6 0 1 .4 1 1 0 1.3.2 2.5.6 3.6.1.3 0 .7-.2 1z"/></svg>416-555 0148</li>
        <li><svg viewBox="0 0 24 24"><path d="M2 5h20v14H2z M2 5l10 8 10-8" /></svg>info@kvlroofing.ca</li>
        <li><svg viewBox="0 0 24 24"><path d="M10.6 13.4a1 1 0 0 1 0-1.4l4-4a1 1 0 1 1 1.4 1.4l-4 4a1 1 0 0 1-1.4 0zM7 21a5 5 0 0 1-3.5-8.5l2.8-2.8 1.4 1.4-2.8 2.8a3 3 0 0 0 4.2 4.2l2.8-2.8 1.4 1.4-2.8 2.8A5 5 0 0 1 7 21zm10.7-6.7-1.4-1.4 2.8-2.8a3 3 0 0 0-4.2-4.2l-2.8 2.8-1.4-1.4 2.8-2.8a5 5 0 0 1 7 7z"/></svg>www.kvlroofing.ca</li>
      </ul>
    </div>
  </section>
  <section class="card card-back">
    <p class="brand-name">KVL Roofing</p>
  </section>
</main>
</body>
</html>
```